Email Signature

Our company is having its 10th anniversary in 2021. We would like a new email signature to celebrate the occasion. Attached is our business card design.
Please refer to our website for actual contact details.
www.corvanhold.com.au

Industry/Entity Type

Real Estate

Requirements
Must have
• Our logo
Email
Contact Numbers
Address
Website address

Celebrating 10 years in 2021
Nice to have
• Something that blends the designs of our website and business card

```html
<!DOCTYPE html>
<html lang="en">
<head>
<meta charset="utf-8">
<title>Corvan Hold – Email Signature</title>
<link rel="stylesheet" href="https://fonts.googleapis.com/css2?family=Arimo:wght@400;700&display=swap">
<style>
  :root {
    --page-bg: #2b2b2b;
    --card-bg: #ffffff;
    --brand-blue: #1b5fa6;
    --brand-blue-light: #2a6db3;
    --ink: #1f1f1f;
    --divider: #555555;
    --white: #ffffff;
  }
  * { box-sizing: border-box; margin: 0; padding: 0; }
  html, body {
    width: 1200px;
    height: 900px;
    overflow: hidden;
    background: var(--page-bg);
    font-family: "Arimo", Arial, sans-serif;
  }
  .signature {
    position: absolute;
    left: 50px;
    top: 292px;
    width: 1100px;
    height: 315px;
    background: var(--card-bg);
    overflow: hidden;
  }
  .brand {
    position: absolute;
    left: 40px;
    top: 90px;
    display: flex;
    align-items: center;
    gap: 12px;
  }
  .brand-mark {
    width: 22px;
    height: 22px;
    background: var(--brand-blue);
  }
  .brand-name {
    font-size: 34px;
    font-weight: 700;
    color: var(--brand-blue);
    letter-spacing: 0.5px;
    white-space: nowrap;
  }
  .divider {
    position: absolute;
    top: 31px;
    width: 2px;
    height: 147px;
    background: var(--divider);
  }
  .divider--first { left: 363px; }
  .divider--second { left: 705px; }

  .person {
    position: absolute;
    left: 393px;
    top: 42px;
    color: var(--ink);
  }
  .person-name {
    font-size: 31px;
    font-weight: 700;
    color: var(--brand-blue);
    line-height: 36px;
  }
  .person-role {
    font-size: 20px;
    line-height: 26px;
  }
  .person-address {
    margin-top: 12px;
    font-size: 20px;
    line-height: 27px;
  }
  .contacts {
    position: absolute;
    left: 742px;
    top: 48px;
    list-style: none;
  }
  .contacts li {
    display: flex;
    align-items: center;
    height: 28.5px;
    font-size: 20px;
    color: var(--ink);
  }
  .contacts svg {
    width: 16px;
    height: 16px;
    margin-right: 10px;
    fill: var(--brand-blue);
    flex: none;
  }
  .skyline {
    position: absolute;
    left: 0;
    top: 196px;
    width: 100%;
    height: 70px;
    background: linear-gradient(to bottom, var(--brand-blue-light), var(--brand-blue));
  }
  .services-band {
    position: absolute;
    left: 0;
    top: 265px;
    width: 100%;
    height: 50px;
    background: var(--brand-blue);
    display: flex;
    align-items: center;
    justify-content: center;
  }
  .services {
    color: var(--white);
    font-size: 19px;
    letter-spacing: 0.3px;
    margin-top: -8px;
  }
</style>
</head>
<body>
  <section class="signature">
    <div class="brand">
      <span class="brand-mark"></span>
      <span class="brand-name">CORVAN HOLD</span>
    </div>

    <span class="divider divider--first"></span>

    <div class="person">
      <p class="person-name">Daniel R, Foster</p>
      <p class="person-role">Owner</p>
      <p class="person-address">Shop 8 / 27 Harbourview Lane<br>Meadowbank, NSW 2114</p>
    </div>

    <span class="divider divider--second"></span>

    <ul class="contacts">
      <li>
        <svg viewBox="0 0 16 16" aria-hidden="true"><path d="M3.5 1.5l2.5 0 1.2 3.2-1.6 1.2c.8 1.8 2.2 3.2 4 4l1.2-1.6 3.2 1.2v2.5c0 .9-.8 1.6-1.7 1.5C6.9 13 3 9.1 2 3.2 1.9 2.3 2.6 1.5 3.5 1.5z"/></svg>
        1300 00CORV(2678)
      </li>
      <li>
        <svg viewBox="0 0 16 16" aria-hidden="true"><path d="M4 1h8v4H4zM1 6h14v6h-3v3H4v-3H1zM5 10v3h6v-3z"/></svg>
        8027 3914
      </li>
      <li>
        <svg viewBox="0 0 16 16" aria-hidden="true"><path d="M1 3h14v10H1zM2.5 4.5L8 9l5.5-4.5v7h-11z" fill-rule="evenodd"/></svg>
        admin@corvanhold.com.au
      </li>
      <li>
        <svg viewBox="0 0 16 16" aria-hidden="true"><circle cx="8" cy="8" r="7"/><path d="M8 1v14M1 8h14" stroke="#fff" stroke-width="1.2"/><ellipse cx="8" cy="8" rx="3" ry="7" fill="none" stroke="#fff" stroke-width="1.2"/></svg>
        www.corvanhold.com.au
      </li>
    </ul>

    <div class="skyline" role="img" aria-label="Blue city skyline silhouette running across the width of the signature"></div>
    <div class="services-band">
      <p class="services">BUILDING MANAGEMENT - CONCIERGE - CARETAKING - CLEANING</p>
    </div>
  </section>
</body>
</html>
```